Exclusive Offer Verbalis December 2022

A design that includes the company logo company and the text set out below. It could be a season design (winter design). it is a short promo to be sent by email. It should express that the promotion is on translation services.

Title: ESPECIAL DICIEMBRE

Information:

10% Descuento del 13 al 16 de diciembre
8% Después del 13 y hasta el 24 de diciembre

En contenidos web, materiales publicitarios, catàlogos, textos legales, manuales y más.

+30 años de experiencia, ISO 17100, traductores nativos

Target Market(s)

B2B Spain - any company that needs translation services

Industry/Entity Type

Services and Translation

Requirements
Must have
• Please take into account our corporate style guide attached
Nice to have
• A design that suggests a special offer from a serious, professional, technological and solid translation company.
Should not have
• Typical Christmas stationery, colours that don't fit into our company design trend.

```html
<!DOCTYPE html>
<html lang="es">
<head>
<meta charset="utf-8">
<title>Especial Diciembre – Verbalis</title>
<link rel="stylesheet" href="https://fonts.googleapis.com/css2?family=Montserrat:ital,wght@0,400;0,500;0,600;0,700;1,600&family=Oswald:wght@400;500&display=swap">
<style>
  :root {
    --page-bg: #a9d6fc;
    --sky-top: #035b9f;
    --sky-bottom: #0a86d8;
    --orange-top: #f2b400;
    --orange-bottom: #f08800;
    --white: #ffffff;
    --navy: #1f4479;
    --steel: #4a6e9b;
    --footer-text: #eef3fa;
  }
  * { margin: 0; padding: 0; box-sizing: border-box; }
  html, body { width: 1200px; height: 1200px; overflow: hidden; }
  body {
    background: var(--page-bg);
    font-family: "Montserrat", Arial, sans-serif;
    position: relative;
  }
  .poster {
    position: absolute;
    left: 249px; top: 30px;
    width: 702px; height: 1140px;
    background: linear-gradient(180deg, var(--sky-top) 0%, var(--sky-bottom) 80%);
    overflow: hidden;
    color: var(--white);
  }
  .ornament-string {
    position: absolute; left: 350px; top: 0;
    width: 2px; height: 42px; background: var(--orange-top);
  }
  .ornament {
    position: absolute; left: 240px; top: 40px;
    width: 222px; height: 222px; border-radius: 50%;
    border: 2px solid var(--orange-top);
    padding: 5px;
  }
  .ornament-ball {
    width: 100%; height: 100%; border-radius: 50%;
    background: linear-gradient(180deg, var(--orange-top), var(--orange-bottom));
    display: flex; flex-direction: column; align-items: center; justify-content: center;
    padding-bottom: 18px;
  }
  .ornament-title {
    font-weight: 700; font-size: 33px; line-height: 37px; text-align: center;
    text-shadow: 0 2px 3px rgba(120,60,0,.35);
  }
  .centered { position: absolute; left: 0; width: 100%; text-align: center; }
  .season { top: 275px; font-family: "Oswald", "Arial Narrow", sans-serif; font-weight: 400; font-size: 41px; }
  .discount { font-family: "Oswald", "Arial Narrow", sans-serif; font-weight: 500; font-size: 50px; line-height: 56px; }
  .discount.first { top: 347px; }
  .discount.second { top: 451px; }
  .dates { font-size: 20px; font-weight: 500; }
  .dates.first { top: 408px; }
  .dates.second { top: 512px; }
  .services {
    position: absolute; left: 66px; top: 563px;
    width: 570px; height: 88px; border-radius: 44px;
    border: 3px solid var(--white);
    background: linear-gradient(180deg, var(--orange-top), var(--orange-bottom));
    display: flex; align-items: center; justify-content: center;
    text-align: center; font-weight: 600; font-size: 19.5px; line-height: 24px;
  }
  .credentials { top: 661px; font-style: italic; font-weight: 600; font-size: 21.5px; line-height: 27px; }
  .winter-scene { position: absolute; left: 0; top: 720px; width: 702px; height: 260px; }
  .snow-ground {
    position: absolute; left: 0; top: 975px; width: 100%; bottom: 41px;
    background: var(--white);
  }
  .brand {
    position: absolute; left: 0; top: 966px; width: 100%;
    display: flex; justify-content: center; align-items: center; gap: 14px;
  }
  .brand-mark { width: 40px; height: 40px; background: var(--steel); }
  .brand-name { color: var(--navy); font-weight: 600; font-size: 32px; line-height: 40px; }
  .social {
    position: absolute; top: 1050px; left: 0; width: 100%;
    display: flex; justify-content: center; gap: 10px; list-style: none;
  }
  .social li {
    width: 30px; height: 30px; border-radius: 50%;
    background: var(--orange-top); border: 2px solid #f3e6c8;
  }
  .footer {
    position: absolute; left: 0; bottom: 0; width: 100%; height: 41px;
    background: var(--steel); color: var(--footer-text);
    display: flex; align-items: center; justify-content: center; gap: 14px;
    font-size: 10.5px;
  }
  .footer b { font-weight: 700; }
</style>
</head>
<body>
  <main class="poster">
    <div class="ornament-string"></div>
    <div class="ornament">
      <div class="ornament-ball">
        <h1 class="ornament-title">Especial<br>Diceiembre</h1>
      </div>
    </div>

    <p class="centered season">Promoción de Temporada</p>
    <p class="centered discount first">10% DESCUENTO</p>
    <p class="centered dates first">del 13 al 16 de diciembre</p>
    <p class="centered discount second">8%</p>
    <p class="centered dates second">del 13 y hasta el 24 de diciembre</p>

    <div class="services">En contenidos web, materiales publicitarios,<br>catàlogos, textos legales, manuales y más.</div>

    <p class="centered credentials">+30 años de experiencia, ISO 17100,<br>traductores nativos</p>

    <svg class="winter-scene" viewBox="0 0 702 260" role="img" aria-label="Illustration of a white snowy forest of fir trees on a hill">
      <defs>
        <linearGradient id="forest-glow" x1="0" y1="0" x2="0" y2="1">
          <stop offset="0" stop-color="#ffffff" stop-opacity="0"/>
          <stop offset="1" stop-color="#ffffff" stop-opacity="0.35"/>
        </linearGradient>
      </defs>
      <rect x="110" y="0" width="480" height="215" fill="url(#forest-glow)"/>
      <path d="M0 210 Q351 196 702 210 L702 260 L0 260 Z" fill="#ffffff"/>
    </svg>
    <div class="snow-ground"></div>

    <div class="brand">
      <span class="brand-mark"></span>
      <span class="brand-name">Verbalis</span>
    </div>

    <ul class="social" aria-label="Redes sociales">
      <li></li><li></li><li></li><li></li>
    </ul>

    <footer class="footer">
      <span><b>P:</b> +34 91 000 12 34</span><span>|</span>
      <span><b>E:</b> info@verbalis.es</span><span>|</span>
      <span><b>W:</b> www.verbalis.es</span><span>|</span>
      <span>C/ Alba 45, 3º - 2ª, 08010 Barcelona</span>
    </footer>
  </main>
</body>
</html>
```